Exterior cleaning company requires a eye catching a5 leaflet

we need some updated leaflet designs, a5 folded, we are targeting all exterior cleaning contracts, including roof cleaning & treatment, render cleaning & Treatment, driveways, block paving cleaning using the latest in low pressure cleaning technologies along side high pressure jetwashing. gutter clearance and flushing, water fed telescopic pole window cleaning of difficult to reach windows and high buildings. our website : www.tkbellowsec.co.uk facebook page: https://www.facebook.com/tkbellowsexteriorcareltd Instagram: https://www.instagram.com/tkbellowsec/ a quick google search of roof cleaning, soft washing etc will provide results of what we are doing

Target Market(s)

home owners, commercial clients

Font styles to use
Serif
Sans Serif

Requirements
Must have
• A5 Landscape folded leaflet, front page with company information and bullet points of main works : window & conservatory cleaning, roof cleaning & treatment, Render cleaning & treatment, pressure washing, soft washing, gutter clearing, pressure washing of patios, driveways, gutters, fascias (more info can be provided on techniques etc if required)

```html
<!DOCTYPE html>
<html lang="en">
<head>
<meta charset="utf-8">
<title>TK Bellows Exterior Care – A5 Leaflet</title>
<link rel="stylesheet" href="https://fonts.googleapis.com/css2?family=Arimo:wght@400;700&family=Roboto:wght@400;500&family=Roboto+Condensed:wght@400;500&family=Encode+Sans+Condensed:wght@300;400&display=swap">
<style>
  :root{
    --bg:#dcd8d5;
    --paper:#f4f4f4;
    --blue:#4b90c9;
    --blue-light:#72b2df;
    --green:#6cbd72;
    --green-light:#9ad49b;
    --green-dark:#3c8c41;
    --ink:#1e1e1e;
    --white:#ffffff;
    --line-blue:#3f86c6;
    --line-green:#4f9a4f;
  }
  *{margin:0;padding:0;box-sizing:border-box}
  html,body{width:1200px;height:939px;overflow:hidden;background:var(--bg)}
  .canvas{position:relative;width:1200px;height:939px}
  .spread{position:absolute;overflow:hidden;background:var(--paper)}
  .spread--outer{left:88px;top:288px;width:499px;height:356px}
  .spread--inner{left:610px;top:287px;width:504px;height:360px;background:linear-gradient(90deg,#e6e6e6 0,#f8f8f8 14px,#f0f0f0 45%,#f8f8f8 55%,#f2f2f2)}
  .abs{position:absolute}

  /* back panel: contact */
  .contact{left:0;top:0;width:129px;height:356px;background:linear-gradient(160deg,var(--blue-light),var(--blue) 70%);color:var(--white);font-family:Arimo,sans-serif;font-weight:700;text-align:center}
  .contact__title{position:absolute;left:6px;top:14px;font-family:Roboto,sans-serif;font-weight:500;font-size:19px;letter-spacing:.2px}
  .contact__rule{position:absolute;left:6px;top:43px;width:95px;height:1px;background:var(--white)}
  .contact__line{position:absolute;left:9px;width:110px;font-size:4.2px;line-height:1.45}
  .contact__foot{position:absolute;left:101px;top:342px;font-size:3.8px;color:var(--white);font-family:Arimo,sans-serif;font-weight:700}

  .photo{position:absolute}
  .circle{border-radius:50%;border:1.5px solid #fff}
  .band{left:129px;top:179px;width:117px;height:64px;background:linear-gradient(180deg,#9a8c86,#7a6a62 55%,#c9c3bd)}
  .map{left:101px;top:243px;width:137px;height:88px;background:linear-gradient(135deg,#e4ece0,#f4f4f2 45%,#eef1ee)}

  /* front cover */
  .cover-photo{left:246px;top:60px;width:253px;height:296px;background:linear-gradient(110deg,#6b7a5a 0%,#8c8f86 28%,#bfc3c6 45%,#dfe2e4 70%,#eceeef 100%)}
  .cover-veil{left:297px;top:126px;width:202px;height:205px;background:rgba(250,250,250,.74)}
  .logo{left:295px;top:8px;width:135px;height:51px;background:#e4e4e4;font-family:"Roboto Condensed",sans-serif;color:var(--ink)}
  .logo__mark{position:absolute;left:7px;top:2px;width:47px;height:47px;border:1px solid var(--ink);border-radius:50%}
  .logo__name{position:absolute;left:62px;top:8px;font-size:14px;font-weight:500;line-height:1}
  .logo__sub{position:absolute;left:62px;top:24px;font-size:6.5px;font-weight:500;line-height:1}
  .logo__tel{position:absolute;left:62px;top:34px;font-size:8px;font-weight:500;line-height:1}
  .services{left:313px;top:183px;list-style:none;font-family:"Encode Sans Condensed",sans-serif;font-weight:300;font-size:9.4px;color:var(--ink);line-height:12.5px;white-space:nowrap}

  /* inside spread */
  .about-title{left:101px;top:13px;font-family:"Encode Sans Condensed",sans-serif;font-weight:400;font-size:16px;color:var(--green-dark);letter-spacing:.3px}
  .about-col{left:30px;top:39px;width:97px;height:311px;background:linear-gradient(180deg,var(--blue),var(--blue-light));color:var(--white);font-family:Arimo,sans-serif;font-weight:700;font-size:3.9px;line-height:1.4;text-align:center}
  .about-col p{position:absolute;left:3px;width:91px}
  .headline{left:142px;top:83px;font-family:"Encode Sans Condensed",sans-serif;font-weight:400;font-size:10px;line-height:13px;color:var(--ink)}
  .house-rule{left:127px;top:220px;width:124px;height:1px;background:var(--line-blue)}
  .house-photo{left:127px;top:221px;width:124px;height:129px;background:linear-gradient(180deg,#c9cdd0 0%,#8e6b5a 40%,#7a4f40 70%,#a8a49c 100%)}
  .house-base{left:127px;top:349px;width:124px;height:1px;background:var(--line-blue)}
  .street-photo{left:251px;top:38px;width:253px;height:140px;background:linear-gradient(100deg,#8b7466,#a08a7c 45%,#6e6a66 70%,#d8dadc 85%,#9a9c9c)}
  .svc{position:absolute;width:74px;font-family:Arimo,sans-serif;font-size:4.2px;line-height:5.9px;color:var(--white);text-align:justify}
  .svc h3{font-size:4.4px;font-weight:700;letter-spacing:.2px;margin-bottom:4px;text-align:left}
</style>
</head>
<body>
<main class="canvas">

  <!-- outer spread: back panel + front cover -->
  <section class="spread spread--outer">
    <div class="abs contact">
      <h2 class="contact__title">Contact us</h2>
      <div class="contact__rule"></div>
      <p class="contact__line" style="top:59px">If you wish to make further enquiries,<br>please contact us on</p>
      <p class="contact__line" style="top:76px">01632 960 418</p>
      <p class="contact__line" style="top:86px">INFO@TKBELLOWSEC.CO.UK</p>
      <p class="contact__line" style="top:106px">14 MARLOW GROVE, EASTBRIDGE,<br>EB4 2LK</p>
      <p class="contact__line" style="top:133px">MISSED US?</p>
      <p class="contact__line" style="top:143px">Don't worry if you were out when we<br>called. You can:</p>
      <p class="contact__line" style="top:169px">SEND A CHEQUE TO OUR ADDRESS.</p>
      <p class="contact__line" style="top:180px">or...</p>
      <p class="contact__line" style="top:190px">BANK TRANSFER:</p>
      <p class="contact__line" style="top:200px">ACCOUNT NUMBER: 12345670</p>
      <p class="contact__line" style="top:210px">SORT CODE: 00-11-22</p>
    </div>

    <div class="photo circle" role="img" aria-label="Photo of a glazed shopfront being cleaned" style="left:139px;top:51px;width:47px;height:47px;background:radial-gradient(circle,#7d8588,#4c5357)"></div>
    <div class="photo circle" role="img" aria-label="Photo of a tall window facade" style="left:177px;top:27px;width:51px;height:51px;background:radial-gradient(circle,#b9bcbe,#6d7173)"></div>
    <div class="photo circle" role="img" aria-label="Photo of a shop front with cleaner at work" style="left:177px;top:74px;width:52px;height:52px;background:radial-gradient(circle,#c7c2ae,#8a8b79)"></div>

    <div class="photo band" role="img" aria-label="Photo of a large brick house with cleaning pole"></div>
    <svg class="abs" style="left:129px;top:172px" width="117" height="16" viewBox="0 0 117 16">
      <path d="M0 14 Q55 0 117 6 L117 0 L0 0 Z" fill="var(--paper)"/>
      <path d="M0 14 Q55 0 117 6" stroke="var(--line-blue)" stroke-width="1" fill="none"/>
      <path d="M0 12 Q55 -2 117 4" stroke="var(--line-green)" stroke-width=".8" fill="none"/>
    </svg>
    <div class="photo map" role="img" aria-label="Street map showing the company location"></div>

    <div class="photo cover-photo" role="img" aria-label="Photo of a modern glass extension and a cleaner using a water fed pole on a patio"></div>
    <svg class="abs" style="left:246px;top:55px" width="253" height="44" viewBox="0 0 253 44">
      <path d="M0 14 Q120 -6 253 38 L253 0 L0 0 Z" fill="var(--paper)"/>
      <path d="M0 14 Q120 -6 253 38" stroke="var(--line-blue)" stroke-width="1.1" fill="none"/>
      <path d="M0 10 Q120 -10 253 33" stroke="var(--line-green)" stroke-width=".8" fill="none"/>
    </svg>
    <div class="abs cover-veil"></div>

    <div class="abs logo">
      <div class="logo__mark"></div>
      <div class="logo__name">TK Bellows</div>
      <div class="logo__sub">Exterior Care Ltd</div>
      <div class="logo__tel">Tel: 01632 960 418</div>
    </div>

    <ul class="abs services">
      <li>WINDOW &amp; CONSERVATORY CLEANING</li>
      <li>ROOF CLEANING &amp; TREATMENT</li>
      <li>RENDER CLEANING &amp; TREATMENT</li>
      <li>SOFT WASHING</li>
      <li>PRESSURE WASHING</li>
      <li>DRIVEWAYS &amp; PATIOS</li>
      <li>GUTTER CLEARING &amp; FLUSHING</li>
      <li>FASCIAS &amp; GUTTERS</li>
      <li>SOLAR PANELS</li>
      <li>INTERNAL WINDOWS</li>
    </ul>

    <span class="contact__foot">ltd.</span>
  </section>

  <!-- inner spread: about us + services -->
  <section class="spread spread--inner">
    <h1 class="abs about-title">ABOUT&nbsp; US</h1>

    <div class="abs about-col">
      <p style="top:4px">T.K Bellows Exterior Care is Eastbridge's most reliable, professional cleaning company who have been providing cleaning services across the North West for 10 years!</p>
      <p style="top:47px">At T.K Bellows, our mission is to lead our sector in providing all of our customers with an outstanding cleaning service that keeps ourselves one step ahead of our competition. All of our staff are uniformed, polite, courteous and always happy to help. We aim to build long lasting relationships with our customers, and offer a 5* customer service team to help resolve any issues that may arise.</p>
      <p style="top:130px">Whether it's to improve overall results or safety, we are always on the lookout for the latest equipment that gives the best finish possible. At T.K Bellows our staff use the reach &amp; wash system, otherwise known as the 'water fed pole'. A technique which compared to traditional window cleaning, reaches your windows and frames safely from the ground, even in hard to reach areas such as above conservatories or dormer windows. This prevents any damage to your property from equipment and prevents accidents.</p>
      <p style="top:233px">We like to keep things simple so our visits to you run as smoothly as possible. Understanding that all of our customers aren't always at home when we call, we have a call ahead / messaging service to let you know that we are due that day so gates / garage doors may be left unlocked should you wish we didn't have to climb over. We also provide a secure, key holding service if you'd prefer.</p>
    </div>

    <p class="abs headline">FOR OVER 10&nbsp; YEARS<br>WE HAVE BEEN<br>PROVIDING<br>EXCELLENCE<br>ALONG OUR<br>DIVERSE RANGE OF<br>SERVICES</p>

    <div class="abs house-rule"></div>
    <div class="photo house-photo" role="img" aria-label="Photo of a modern brick house with large windows being cleaned from the garden"></div>
    <div class="abs house-base"></div>

    <div class="photo street-photo" role="img" aria-label="Photo of a period brick house with a company van parked outside"></div>
    <svg class="abs" style="left:251px;top:160px" width="253" height="200" viewBox="0 0 253 200">
      <defs>
        <linearGradient id="greenFade" x1="0" y1="0" x2="1" y2="1">
          <stop offset="0" stop-color="var(--green-light)"/>
          <stop offset="1" stop-color="var(--green)"/>
        </linearGradient>
      </defs>
      <path d="M0 10 Q130 -8 253 44 L253 0 L0 0 Z" fill="var(--paper)"/>
      <path d="M11 9 Q130 -6 253 46 L253 200 L11 200 Z" fill="url(#greenFade)"/>
    </svg>

    <div class="svc" style="left:268px;top:175px">
      <h3>EXTERNAL WINDOWS</h3>
      <p>Our staff use the reach &amp; washes system otherwise known as the 'water fed pole'. A technique which compared to traditional window cleaning, enabling us to reach your windows and frames safely from the ground.</p>
    </div>
    <div class="svc" style="left:268px;top:246px">
      <h3>INTERNAL WINDOWS</h3>
      <p>We clean internal windows and mirrors using the dragon fly system. This method also using purified water can reach them hard to access windows again safely from the ground.</p>
    </div>
    <div class="svc" style="left:268px;top:305px">
      <h3>CONSERVATORY ROOFS</h3>
      <p>Has your conservatory roof started to turn green, full of bird muck or dirt? Our water pole method 99% of the time gets rid of all the dirt and grime build up left on your roof.</p>
    </div>

    <div class="svc" style="left:348px;top:175px">
      <h3>SOLAR PANELS</h3>
      <p>Using our access equipment we can clean your solar panels. Anything that blocks the light transmission to your solar PV (or thermal) panels has the potential to lower the performance.</p>
    </div>
    <div class="svc" style="left:348px;top:240px">
      <h3>FASCIAS &amp; GUTTERS</h3>
      <p>Using our telescopic pressure washing lance, we can clean all of your UPVC fascia's, gutters and drain pipes safely from the ground. The end result your fascia's and gutters looking like brand new again.</p>
    </div>
    <div class="svc" style="left:348px;top:311px">
      <h3>DRIVEWAYS &amp; PATIOS</h3>
      <p>From small patio areas to large driveways we clean it all. T.K Bellows specialise in all driveway and patio cleaning from Indian stone, tarmac, concrete flags to block paving.</p>
    </div>

    <div class="svc" style="left:425px;top:210px">
      <h3>GUTTER CLEANING</h3>
      <p>Your property's gutters and downpipes accumulate all sorts of debris brought by the wind. Using our high reach vac we can clean the gutters safely from the ground eliminating any falls from height.</p>
    </div>
    <div class="svc" style="left:425px;top:281px">
      <h3>PRESSURE WASHING</h3>
      <p>We offer a wide range of pressure washing services from garden furniture to house roofs at competitive prices. Cleaning and restoration of all hard surfaces in both the domestic and commercial market.</p>
    </div>
  </section>

</main>
</body>
</html>
```